Brivane Redesign

We need a face lift for our website, www.brivane.com. We sell flooring and related products nationwide. We are interested in expanding the width of the website and introducing grays and black. We want the design to be both contemporary and user friendly.

```html
<!DOCTYPE html>
<html lang="en">
<head>
<meta charset="utf-8">
<title>Brivane – Flooring Values Online</title>
<link href="https://fonts.googleapis.com/css2?family=Oswald:wght@300;400;700&family=Arimo:wght@400;700&family=Open+Sans:wght@400;600&display=swap" rel="stylesheet">
<style>
:root{
  --backdrop:#ececec;
  --paper:#ffffff;
  --nav:#8a8a8a;
  --side-head:#7e7e7e;
  --side-body:#d9d9d9;
  --ink:#222222;
  --ink-soft:#555555;
  --rule:#444444;
  --promo:#1c1c1c;
  --btn:#b3aa9c;
  --accent:#a8977a;
  --link:#1a5fb4;
  --price:#6f6f6f;
}
*{margin:0;padding:0;box-sizing:border-box}
html,body{width:1108px;height:1200px;overflow:hidden;background:var(--backdrop)}
.stage{width:1200px;height:1300px;transform:scale(.92333);transform-origin:0 0;position:relative;font-family:"Arimo",Arial,sans-serif;color:var(--ink)}
.sheet{position:absolute;left:107px;top:33px;width:983px;height:1237px;background:var(--paper)}
.abs{position:absolute}
/* header */
.logo{left:122px;top:56px;display:flex;align-items:center;gap:8px}
.logo-mark{width:34px;height:34px;background:#5a5a5a}
.logo-name{font-family:"Arimo",sans-serif;font-size:32px;font-weight:700;color:#2a2a2a;letter-spacing:-1px}
.tagline{left:176px;top:101px;font-size:10px;font-weight:700;color:#2a2a2a}
.util-links{left:568px;top:63px;font-size:11px;color:#555}
.search{left:393px;top:82px;width:348px;height:32px;border:1px solid #d4d4d4;background:#f4f4f4;font-size:12px;color:#777;padding:9px 15px}
.search svg{position:absolute;right:14px;top:8px}
.cart{right:137px;top:61px;font-size:12px;color:var(--accent);display:flex;gap:8px;align-items:center}
.phone{right:136px;top:79px;font-size:25px;font-weight:700;color:#2a2a2a}
.chat{right:136px;top:113px;font-size:12px;color:#222}
.chat b{color:var(--accent);font-weight:400}
/* nav */
.nav{left:107px;top:140px;width:983px;height:38px;background:var(--nav);display:flex;justify-content:space-between;align-items:center;padding:0 26px 0 21px;list-style:none}
.nav li{font-family:"Oswald",sans-serif;font-weight:300;font-size:17px;color:#fff;letter-spacing:-.3px}
/* sidebar */
.promo{left:107px;top:183px;width:270px;height:146px;background:var(--promo);padding:14px 18px;color:#fff}
.promo h2{font-family:"Oswald",sans-serif;font-weight:300;font-size:25px;letter-spacing:-1px;line-height:1}
.promo p{font-size:12px;line-height:14.5px;margin-top:13px}
.promo .btn{display:inline-block;margin-top:14px;background:var(--btn);color:#1c1c1c;font-size:12px;padding:5px 15px}
.side-block{left:107px;width:270px;background:var(--side-body)}
.side-block h3{background:var(--side-head);color:#fff;font-family:"Oswald",sans-serif;font-weight:300;font-size:19px;letter-spacing:-.8px;height:32px;line-height:32px;padding-left:16px}
.side-block ul{list-style:none;padding:6px 20px 0 17px}
.side-block li{font-size:12px;height:25px;line-height:28px;border-bottom:1px solid var(--rule);padding-left:16px;position:relative}
.side-block li::before{content:"";position:absolute;left:2px;top:11px;border-left:5px solid #222;border-top:3px solid transparent;border-bottom:3px solid transparent}
/* main visuals */
.hero{left:393px;top:183px;width:697px;height:418px;background:linear-gradient(180deg,#b9a58a 0%,#7a5a3f 35%,#6b4a32 55%,#cfcac3 75%,#dcd8d2 100%)}
.dots{left:1032px;top:584px;display:flex;gap:6px}
.dots i{width:10px;height:10px;border-radius:50%;background:#fff}
.dots i:first-child{background:#222}
.sale{left:387px;top:617px;width:344px;height:138px;background:linear-gradient(100deg,#c9a46e,#b58749 55%,#d2b27f);overflow:hidden}
.sale .ribbon{position:absolute;left:-46px;top:40px;width:210px;height:34px;background:rgba(255,255,255,.35);transform:rotate(-45deg);color:#fff;font-family:"Oswald",sans-serif;font-weight:300;font-size:18px;text-align:center;line-height:34px}
.sale .big{position:absolute;left:140px;top:4px;width:200px;text-align:center;color:#fff;font-family:"Oswald",sans-serif;font-style:normal}
.sale .big span{display:block;font-size:34px;font-weight:300;line-height:40px}
.sale .big strong{display:block;font-size:46px;font-weight:700;line-height:50px;letter-spacing:3px}
.sale .ends{position:absolute;left:133px;top:104px;font-size:23px;font-weight:700;color:#111}
.samples{left:747px;top:617px;width:344px;height:138px;background:#fff;border:1px solid #e3e3e3;overflow:hidden}
.samples .wood{position:absolute;right:0;top:0;width:166px;height:100px;background:linear-gradient(160deg,#e4c7a1,#a5714a 60%,#6d4a30)}
.samples h4{position:absolute;left:16px;top:12px;font-family:"Oswald",sans-serif;line-height:1}
.samples h4 b{display:block;font-size:48px;font-weight:700;color:#1c1c1c;letter-spacing:2px}
.samples h4 span{display:block;font-size:36px;font-weight:300;color:#555;letter-spacing:1px;margin-top:-2px}
.samples .note{position:absolute;left:0;bottom:0;width:100%;height:38px;background:#e6e6e6;font-family:"Open Sans",sans-serif;font-size:15.5px;letter-spacing:.1px;color:#777;padding:0 14px;line-height:38px;white-space:nowrap}
.card{top:771px;width:228px;height:246px;background:#fff}
.card .photo{height:154px}
.card .brand{position:absolute;left:9px;top:163px;font-family:"Open Sans",sans-serif;font-weight:600;font-size:14px;color:#777}
.card .line{position:absolute;left:9px;top:178px;font-family:"Open Sans",sans-serif;font-size:11.5px;color:#888}
.card .price{position:absolute;left:9px;top:203px;height:33px;background:var(--price);color:#fff;font-family:"Oswald",sans-serif;font-weight:300;font-size:19px;padding:2px 8px;line-height:29px;letter-spacing:-.5px}
.card .price b{font-weight:700}
/* footer */
.legal{left:107px;top:1046px;width:983px;height:32px;background:#dcdcdc;font-size:11px;text-align:center;line-height:32px;color:#222}
.foot-links{left:360px;top:1110px;width:420px;text-align:center;font-size:12px;line-height:17px;color:#444}
.foot-links a{color:var(--link)}
.badge{position:absolute;background:#d8d8d8}
</style>
</head>
<body>
<div class="stage">
  <div class="sheet"></div>

  <header>
    <div class="abs logo"><span class="logo-mark"></span><span class="logo-name">Brivane.com</span></div>
    <div class="abs tagline">Values Online Since '99</div>
    <div class="abs util-links">Order Tracking | FAQ | My Account</div>
    <div class="abs search">search product or item #
      <svg width="18" height="18" viewBox="0 0 18 18"><circle cx="7" cy="7" r="5" fill="none" stroke="#666" stroke-width="2"/><line x1="11" y1="11" x2="16" y2="16" stroke="#666" stroke-width="2.5"/></svg>
    </div>
    <div class="abs cart">
      <svg width="16" height="12" viewBox="0 0 16 12"><path d="M0 1h3l2 7h8l2-5H4" fill="none" stroke="#a8977a" stroke-width="1.6"/><circle cx="6" cy="10.5" r="1.3" fill="#a8977a"/><circle cx="12" cy="10.5" r="1.3" fill="#a8977a"/></svg>
      0 Product(s) in cart
    </div>
    <div class="abs phone">1-888-555-0147</div>
    <div class="abs chat">LIVE CHAT <b>OFFLINE</b></div>
  </header>

  <ul class="abs nav">
    <li>LAMINATE</li><li>HARDWOOD</li><li>AREA RUGS</li><li>BAMBOO</li><li>CORK</li><li>VINYL</li><li>CARPET TILE</li><li>TILE</li><li>CLOCKS</li><li>BATH</li><li>CLEARANCE</li>
  </ul>

  <aside>
    <div class="abs promo">
      <h2>CURRENT PROMOS</h2>
      <p>Offering discount prices on laminate, hardwood, cork, bamboo, vinyl and area rugs from the brands you know and trust.</p>
      <span class="btn">CHECK PROMOS!</span>
    </div>
    <div class="abs side-block" style="top:333px;height:225px">
      <h3>SHOP BY BRAND</h3>
      <ul><li>Laminate</li><li>Hardwood</li><li>Bamboo</li><li>Cork</li><li>Vinyl</li><li>Carpet Tile</li><li>Tile</li></ul>
    </div>
    <div class="abs side-block" style="top:563px;height:126px">
      <h3>HOME DECOR</h3>
      <ul><li>Area Rugs</li><li>Bath</li><li>Clocks</li></ul>
    </div>
    <div class="abs side-block" style="top:693px;height:150px">
      <h3>ACCESSORIES</h3>
      <ul><li>Underlayment</li><li>Trim &amp; Molding</li><li>Floor Cleaner</li><li>Installation Tools</li></ul>
    </div>
    <div class="abs side-block" style="top:847px;height:170px">
      <h3>FLOORING FACTS</h3>
      <ul><li>Laminate</li><li>Hardwood</li><li>Cork</li><li>Area Rugs</li></ul>
    </div>
  </aside>

  <main>
    <div class="abs hero" role="img" aria-label="Modern kitchen with walnut cabinets and light stone tile floor"></div>
    <div class="abs dots"><i></i><i></i><i></i></div>

    <div class="abs sale" role="img" aria-label="Sitewide sale banner over a light wood floor">
      <div class="ribbon">FREE SHIPPING</div>
      <div class="big"><span>sitewide</span><strong>SALE</strong></div>
      <div class="ends">ends monday!</div>
    </div>

    <div class="abs samples">
      <div class="wood" role="img" aria-label="Stack of wood flooring sample planks"></div>
      <h4><b>FREE</b><span>SAMPLES</span></h4>
      <div class="note">Completely free. No credit card required</div>
    </div>

    <div class="abs card" style="left:387px">
      <div class="photo" role="img" aria-label="Living room with warm oak laminate floor" style="background:linear-gradient(180deg,#8a9aa8,#6b4a35 40%,#c08a55 70%,#d9a36a)"></div>
      <div class="brand">Hallbrook</div>
      <div class="line">Seaside Haven 12mm Laminate</div>
      <div class="price">starting at <b>2.49 sq.ft.</b></div>
    </div>
    <div class="abs card" style="left:625px">
      <div class="photo" role="img" aria-label="Hallway with slate-look luxury vinyl tile" style="background:linear-gradient(180deg,#8b6a4b,#6d5846 45%,#6a6558 70%,#4e4b43)"></div>
      <div class="brand">Verrant</div>
      <div class="line">Stoneform Luxury Vinyl Tile</div>
      <div class="price">starting at <b>3.79 sq.ft.</b></div>
    </div>
    <div class="abs card" style="left:863px">
      <div class="photo" role="img" aria-label="Patio lounge with weathered wood laminate floor" style="background:linear-gradient(180deg,#a8c4d6,#c7b8a6 40%,#9b8270 65%,#7d6656)"></div>
      <div class="brand">Hallbrook</div>
      <div class="line">Seaside Haven 12mm Laminate</div>
      <div class="price">starting at <b>4.99 sq.ft.</b></div>
    </div>
  </main>

  <footer>
    <div class="abs legal">©1999-2014 Northgate Home Supply, Inc. All rights reserved. BRIVANE, BRIVANE OUTLET, and BRIVANE.COM are trademarks of Northgate Home Supply, Inc. or its affiliates.</div>
    <div class="abs foot-links">
      <a>about us</a> | <a>careers</a> | <a>consumer reviews</a> | <a>contact us</a> | <a>faq</a><br>
      <a>ordering</a> | <a>pricing</a> | <a>privacy policy</a> | <a>return policy</a> | <a>shipping</a> | <a>sitemap</a>
    </div>
    <span class="badge" style="left:260px;top:1105px;width:70px;height:40px"></span>
    <span class="badge" style="left:792px;top:1107px;width:126px;height:36px;border-radius:18px"></span>
    <span class="badge" style="left:350px;top:1152px;width:60px;height:48px;border-radius:50%"></span>
    <span class="badge" style="left:446px;top:1171px;width:42px;height:28px"></span>
    <span class="badge" style="left:494px;top:1171px;width:42px;height:28px"></span>
    <span class="badge" style="left:542px;top:1171px;width:42px;height:28px"></span>
    <span class="badge" style="left:590px;top:1171px;width:42px;height:28px"></span>
    <span class="badge" style="left:638px;top:1171px;width:42px;height:28px"></span>
    <span class="badge" style="left:686px;top:1171px;width:44px;height:28px"></span>
    <span class="badge" style="left:768px;top:1153px;width:50px;height:50px;border-radius:50%"></span>
    <span class="badge" style="left:447px;top:1216px;width:66px;height:26px"></span>
    <span class="badge" style="left:540px;top:1216px;width:70px;height:38px"></span>
    <span class="badge" style="left:638px;top:1210px;width:82px;height:42px"></span>
  </footer>
</div>
</body>
</html>
```